Velmin & Co Powerpoint Template

A simple powerpoint template for my business which provides management consulting services for Business Owners.

It should reflect the colours within the logo design and should work as the master template for all standard powerpoint slide layouts.

```html
<!DOCTYPE html>
<html lang="en">
<head>
<meta charset="utf-8">
<title>Velmin &amp; Co – Presentation Template</title>
<link rel="stylesheet" href="https://fonts.googleapis.com/css2?family=Poppins:wght@300;400;500;600;700&display=swap">
<style>
:root{
  --orange:#e2591f;
  --ink:#262626;
  --text:#4a4a4a;
  --muted:#7a7a7a;
  --band:#4b4b4b;
  --mint:#eef4f2;
  --white:#ffffff;
  --board:#c4c4c4;
  --track:#ececec;
  --dark-a:#1c1e21;
  --dark-b:#3b3e42;
  --stage:#dde1e7;
}
*{box-sizing:border-box;margin:0;padding:0}
html,body{width:1200px;height:2766px;overflow:hidden}
body{position:relative;font-family:"Poppins",sans-serif;color:var(--text);background:var(--board)}

.hero{position:absolute;left:0;top:0;width:1200px;height:730px;background:var(--stage)}
.board{position:absolute;left:0;top:730px;width:1200px;height:2036px;background:var(--board)}

/* brand lockup: one line name with a dot */
.brand{position:absolute;display:flex;align-items:center;gap:7px;color:var(--ink);white-space:nowrap}
.slide--dark .brand,.slide--dark .brand-tag{color:var(--white)}
.brand-dot{width:9px;height:9px;border-radius:50%;background:var(--orange);flex:none}
.brand-name{font-weight:500;font-size:16px;line-height:1;color:inherit}
.brand-tag{position:absolute;font-weight:400;font-size:6.5px;letter-spacing:.2px;color:var(--ink);white-space:nowrap}
.brand--hero{left:930px;top:96px;gap:12px}
.brand--hero .brand-dot{width:16px;height:16px}
.brand--hero .brand-name{font-size:30px}
.brand-tag--hero{left:930px;top:142px;font-size:12.5px}
.brand--mini{gap:5px}
.brand--mini .brand-dot{width:6px;height:6px}
.brand--mini .brand-name{font-size:8px}

/* slides */
.slide{position:absolute;width:563px;height:316px;background:var(--white);overflow:hidden;color:var(--ink)}
.slide--hero{left:196px;top:118px;transform:scale(.86);transform-origin:top left;box-shadow:0 10px 30px rgba(0,0,0,.18)}
.col-l{left:28px}.col-r{left:609px}
.row-1{top:746px}.row-2{top:1081px}.row-3{top:1416px}.row-4{top:1751px}.row-5{top:2086px}.row-6{top:2421px}

.photo-dark{position:absolute;inset:0;background:linear-gradient(135deg,var(--dark-a) 0%,var(--dark-b) 55%,#17181a 100%)}
.slide--dark{color:var(--white)}

.title{position:absolute;left:51px;font-size:24px;line-height:1.16;color:var(--orange)}
.title b{font-weight:700;display:block}
.title span{font-weight:400;display:block}
.title--bold span{font-weight:700}
.subtitle{position:absolute;left:51px;font-size:11px;font-weight:400;color:inherit}
.date{position:absolute;left:51px;font-size:6.5px;letter-spacing:1.6px;color:inherit}
.date--plain{letter-spacing:0;font-size:5.5px}

.foot-band{position:absolute;left:0;bottom:0;width:100%;height:24px;background:var(--band);color:var(--white);font-size:5.5px;display:flex;align-items:center;justify-content:center}
.foot-band--mint{background:var(--mint);color:var(--ink)}
.foot-band b{font-weight:700;margin-right:2px}

.panel{position:absolute;left:0;background:var(--mint);color:var(--ink)}
.panel-bar{position:absolute;left:51px;height:8px;width:249px;background:var(--orange)}

/* content slides */
.heading{position:absolute;left:36px;top:34px;font-size:13.5px;font-weight:400;color:var(--text)}
.heading b{font-weight:600}
.heading::after{content:"";position:absolute;left:0;top:25px;width:28px;height:3px;background:var(--orange)}
.heading--center{left:0;width:100%;text-align:center}
.heading--center::after{left:50%;margin-left:-14px}
.body{position:absolute;font-size:6.4px;line-height:1.22;color:var(--text)}
.body p{margin-bottom:5px}
.sub{font-size:9px;font-weight:400;color:var(--orange);margin-bottom:7px}
.sub b{font-weight:600}
.bullets{list-style:none}
.bullets li{position:relative;padding-left:12px;margin-bottom:5px}
.bullets li::before{content:"";position:absolute;left:2px;top:2px;width:3px;height:3px;border-radius:50%;background:var(--orange)}
.photo{position:absolute}
.foot-copy{position:absolute;right:15px;top:282px;display:flex;align-items:center;gap:6px;font-size:5px;color:var(--ink)}
.foot-copy b{font-weight:700}
.page-no{width:9px;height:9px;background:var(--orange);color:var(--white);font-size:4.5px;display:flex;align-items:center;justify-content:center}

.donut-label{position:absolute;width:110px;text-align:center;font-size:5.5px;line-height:1.2;color:var(--text)}
.legend{position:absolute;left:317px;width:202px;height:42px;border:1px solid #e3e3e3;border-radius:4px;font-size:5.5px;line-height:1.2;padding:9px 10px 0 20px;color:var(--text)}
.legend-key{position:absolute;left:-5px;top:13px;width:9px;height:9px}

.contact-h{position:absolute;left:48px;top:168px;font-size:11px;font-weight:700;color:var(--orange)}
.contact-list{position:absolute;left:48px;top:190px;list-style:none;font-size:7px;color:inherit}
.contact-list li{display:flex;align-items:center;gap:8px;height:16px}
.contact-list svg{width:9px;height:9px;flex:none}
</style>
</head>
<body>

<section class="hero">
  <div class="slide slide--hero">
    <div class="brand" style="left:51px;top:84px"><span class="brand-dot"></span><span class="brand-name">Velmin &amp; Co</span></div>
    <div class="brand-tag" style="left:51px;top:106px">Advisory for Business Owners</div>
    <h1 class="title" style="top:158px"><b>Presentation Title</b><span>Goes Here</span></h1>
    <p class="subtitle" style="top:220px">Subtitle of Presentation Goes Here</p>
    <p class="date" style="top:246px">Friday, September 1, 2023</p>
    <div class="foot-band"><b>© Velmin &amp; Co</b> 2023. All Rights Reserved.</div>
  </div>
  <div class="brand brand--hero"><span class="brand-dot"></span><span class="brand-name">Velmin &amp; Co</span></div>
  <div class="brand-tag brand-tag--hero">Advisory for Business Owners</div>
</section>

<section class="board"></section>

<!-- title, light -->
<div class="slide col-l row-1">
  <div class="brand" style="left:51px;top:84px"><span class="brand-dot"></span><span class="brand-name">Velmin &amp; Co</span></div>
  <div class="brand-tag" style="left:51px;top:106px">Advisory for Business Owners</div>
  <h1 class="title" style="top:158px"><b>Presentation Title</b><span>Goes Here</span></h1>
  <p class="subtitle" style="top:220px">Subtitle of Presentation Goes Here</p>
  <p class="date" style="top:246px">Friday, September 1, 2023</p>
  <div class="foot-band"><b>© Velmin &amp; Co</b> 2023. All Rights Reserved.</div>
</div>

<!-- title, dark -->
<div class="slide slide--dark col-r row-1">
  <div class="photo-dark" role="img" aria-label="Dark photo of business people shaking hands over a laptop"></div>
  <div class="brand" style="left:51px;top:84px"><span class="brand-dot"></span><span class="brand-name">Velmin &amp; Co</span></div>
  <div class="brand-tag" style="left:51px;top:106px">Advisory for Business Owners</div>
  <h1 class="title" style="top:158px"><b>Presentation Title</b><span>Goes Here</span></h1>
  <p class="subtitle" style="top:220px">Subtitle of Presentation Goes Here</p>
  <p class="date" style="top:246px">Friday, September 1, 2023</p>
  <div class="foot-band foot-band--mint"><b>© Velmin &amp; Co</b> 2023. All Rights Reserved.</div>
</div>

<!-- title, panel left -->
<div class="slide slide--dark col-l row-2">
  <div class="photo-dark" role="img" aria-label="Dark photo of a laptop showing financial charts"></div>
  <div class="panel" style="top:92px;width:361px;height:131px">
    <h1 class="title title--bold" style="top:10px"><b>Presentation Title</b><span>Goes Here</span></h1>
    <p class="subtitle" style="top:72px">Subtitle of Presentation Goes Here</p>
    <p class="date date--plain" style="top:100px">Friday, September 1, 2023</p>
  </div>
  <div class="panel-bar" style="top:219px"></div>
  <div class="brand" style="left:396px;top:140px"><span class="brand-dot"></span><span class="brand-name">Velmin &amp; Co</span></div>
  <div class="brand-tag" style="left:396px;top:162px">Advisory for Business Owners</div>
</div>

<!-- title, panel wide -->
<div class="slide slide--dark col-r row-2">
  <div class="photo-dark" role="img" aria-label="Dark photo of a laptop showing financial charts"></div>
  <div class="brand" style="left:51px;top:54px"><span class="brand-dot"></span><span class="brand-name">Velmin &amp; Co</span></div>
  <div class="brand-tag" style="left:51px;top:76px">Advisory for Business Owners</div>
  <div class="panel" style="top:118px;width:414px;height:133px">
    <h1 class="title title--bold" style="top:10px"><b>Presentation Title</b><span>Goes Here</span></h1>
    <p class="subtitle" style="top:72px">Subtitle of Presentation Goes Here</p>
    <p class="date date--plain" style="top:100px">Friday, September 1, 2023</p>
  </div>
  <div class="panel-bar" style="top:247px"></div>
</div>

<!-- text + photo -->
<div class="slide col-l row-3">
  <h2 class="heading"><b>Heading</b> Goes Here</h2>
  <div class="body" style="left:36px;top:80px;width:204px">
    <p>Duis eget tellus porta, consequat lacus vitae, venenatis dolor. Nulla facilisi. In et sollicitudin lacus. Donec risus orci, gravida sit amet risus vehicula, aliquet pretium sapien. Nullam sit amet magna non ex bibendum mollis. Nunc vel neque eu augue dignissim congue ut vitae magna. Phasellus eget commodo arcu.</p>
    <ul class="bullets">
      <li>Lorem ipsum dolor sit amet, consectetur adipiscing elit. Vivamus eu dui ex. Curabitur dapibus dignissim dui, in molestie metus feugiat sed.</li>
      <li>Duis eget tellus porta, consequat lacus vitae, venenatis dolor.</li>
      <li>Nulla facilisi. In et sollicitudin lacus. Donec risus orci, gravida sit amet risus vehicula, aliquet pretium sapien.</li>
      <li>Duis eget tellus porta, consequat lacus vitae, venenatis dolor. Nulla facilisi.</li>
      <li>In et sollicitudin lacus. Donec risus orci, gravida sit amet risus vehicula, aliquet pretium sapien.</li>
    </ul>
  </div>
  <div class="photo" style="left:301px;top:0;width:225px;height:264px;background:linear-gradient(160deg,#d9dce2,#8d8f94 60%,#5c5e63)" role="img" aria-label="Photo of hands reviewing documents at a desk"></div>
  <div class="brand brand--mini" style="left:16px;top:282px"><span class="brand-dot"></span><span class="brand-name">Velmin &amp; Co</span></div>
  <div class="foot-copy"><span><b>© Velmin &amp; Co</b> 2023. All Rights Reserved.</span><span class="page-no">5</span></div>
</div>

<!-- two columns text -->
<div class="slide col-r row-3">
  <h2 class="heading"><b>Heading</b> Goes Here</h2>
  <div class="body" style="left:36px;top:80px;width:232px">
    <h3 class="sub"><b>Heading</b> Goes Here</h3>
    <p>Lorem ipsum dolor sit amet, consectetur adipiscing elit. Vivamus eu dui ex. Curabitur dapibus dignissim dui, in molestie metus feugiat sed. Praesent aliquet lorem ex, eu dapibus odio varius at.</p>
    <p>Duis eget tellus porta, consequat lacus vitae, venenatis dolor. Nulla facilisi. In et sollicitudin lacus. Donec risus orci, gravida sit amet risus vehicula, aliquet pretium sapien. Nullam sit amet magna non ex bibendum mollis. Nunc vel neque eu augue dignissim congue ut vitae magna. Phasellus eget commodo arcu.</p>
    <p>Nunc vitae semper dui. Integer venenatis, tellus sit amet interdum pretium, erat neque rhoncus turpis, a aliquam augue ligula eget erat.</p>
    <p>Nunc placerat, arcu nec mattis fermentum, nisi mauris convallis nunc, ut luctus nunc nisl id ex.</p>
  </div>
  <div class="body" style="left:296px;top:80px;width:232px">
    <h3 class="sub"><b>Heading</b> Goes Here</h3>
    <p>Lorem ipsum dolor sit amet, consectetur adipiscing elit. Vivamus eu dui ex. Curabitur dapibus dignissim dui, in molestie metus feugiat sed. Praesent aliquet lorem ex, eu dapibus odio varius at.</p>
    <p>Duis eget tellus porta, consequat lacus vitae, venenatis dolor. Nulla facilisi. In et sollicitudin lacus. Donec risus orci, gravida sit amet risus vehicula, aliquet pretium sapien. Nullam sit amet magna non ex bibendum mollis. Nunc vel neque eu augue dignissim congue ut vitae magna. Phasellus eget commodo arcu.</p>
    <p>Nunc vitae semper dui. Integer venenatis, tellus sit amet interdum pretium, erat neque rhoncus turpis, a aliquam augue ligula eget erat.</p>
    <p>Nunc placerat, arcu nec mattis fermentum, nisi mauris convallis nunc, ut luctus nunc nisl id ex.</p>
  </div>
  <div class="brand brand--mini" style="left:16px;top:282px"><span class="brand-dot"></span><span class="brand-name">Velmin &amp; Co</span></div>
  <div class="foot-copy"><span><b>© Velmin &amp; Co</b> 2023. All Rights Reserved.</span><span class="page-no">6</span></div>
</div>

<!-- photo top, centered text -->
<div class="slide col-l row-4">
  <div class="photo" style="left:0;top:0;width:563px;height:145px;background:linear-gradient(170deg,#f3f3f6,#e2e4ea 55%,#cfd2d8)" role="img" aria-label="Photo of a hand with a pen over printed bar charts"></div>
  <h2 class="heading heading--center" style="top:160px"><b>Heading</b> Goes Here</h2>
  <div class="body" style="left:34px;top:198px;width:495px;text-align:center;font-size:6px">
    <p>Lorem ipsum dolor sit amet, consectetur adipiscing elit. Vivamus eu dui ex. Curabitur dapibus dignissim dui, in molestie metus feugiat sed. Praesent aliquet lorem ex, eu dapibus odio varius at. Duis eget tellus porta, consequat lacus vitae, venenatis dolor. Nulla facilisi. In et sollicitudin lacus. Donec risus orci, gravida sit amet risus vehicula, aliquet pretium sapien. Nullam sit amet magna non ex bibendum mollis. Nunc vel neque eu augue dignissim congue ut vitae magna. Phasellus eget commodo arcu. Nunc vitae semper dui. Integer venenatis, tellus sit amet interdum pretium, erat neque rhoncus turpis, a aliquam augue ligula eget erat. Nunc placerat, arcu nec mattis fermentum, nisi mauris convallis nunc, ut luctus nunc nisl id ex. Nam semper tristique mauris, et vestibulum leo fringilla vel.</p>
  </div>
  <div class="brand brand--mini" style="left:16px;top:282px"><span class="brand-dot"></span><span class="brand-name">Velmin &amp; Co</span></div>
  <div class="foot-copy"><span><b>© Velmin &amp; Co</b> 2023. All Rights Reserved.</span><span class="page-no">7</span></div>
</div>

<!-- two columns bullets -->
<div class="slide col-r row-4">
  <h2 class="heading"><b>Heading</b> Goes Here</h2>
  <div class="body" style="left:36px;top:80px;width:232px">
    <h3 class="sub"><b>Heading</b> Goes Here</h3>
    <ul class="bullets">
      <li>Lorem ipsum dolor sit amet, consectetur adipiscing elit. Vivamus eu dui ex. Curabitur dapibus dignissim dui, in molestie metus feugiat sed.</li>
      <li>Duis eget tellus porta, consequat lacus vitae, venenatis dolor.</li>
      <li>Nulla facilisi. In et sollicitudin lacus. Donec risus orci, gravida sit amet risus vehicula, aliquet pretium sapien.</li>
      <li>Nullam sit amet magna non ex bibendum mollis. Nunc vel neque eu augue dignissim congue ut vitae magna. Phasellus eget commodo arcu.</li>
      <li>Nunc vitae semper dui. Integer venenatis, tellus sit amet interdum pretium, erat neque rhoncus turpis, a aliquam augue ligula eget erat.</li>
    </ul>
  </div>
  <div class="body" style="left:296px;top:80px;width:232px">
    <h3 class="sub"><b>Heading</b> Goes Here</h3>
    <ul class="bullets">
      <li>Lorem ipsum dolor sit amet, consectetur adipiscing elit. Vivamus eu dui ex. Curabitur dapibus dignissim dui, in molestie metus feugiat sed.</li>
      <li>Duis eget tellus porta, consequat lacus vitae, venenatis dolor.</li>
      <li>Nulla facilisi. In et sollicitudin lacus. Donec risus orci, gravida sit amet risus vehicula, aliquet pretium sapien.</li>
      <li>Nullam sit amet magna non ex bibendum mollis. Nunc vel neque eu augue dignissim congue ut vitae magna. Phasellus eget commodo arcu.</li>
      <li>Nunc vitae semper dui. Integer venenatis, tellus sit amet interdum pretium, erat neque rhoncus turpis, a aliquam augue ligula eget erat.</li>
    </ul>
  </div>
  <div class="brand brand--mini" style="left:16px;top:282px"><span class="brand-dot"></span><span class="brand-name">Velmin &amp; Co</span></div>
  <div class="foot-copy"><span><b>© Velmin &amp; Co</b> 2023. All Rights Reserved.</span><span class="page-no">8</span></div>
</div>

<!-- donut stats -->
<div class="slide col-l row-5">
  <h2 class="heading"><b>Heading</b> Goes Here</h2>
  <div class="body" style="left:36px;top:80px;width:172px">
    <p>Lorem ipsum dolor sit amet, consectetur adipiscing elit. Vivamus eu dui ex. Curabitur dapibus dignissim dui, in molestie metus feugiat sed. Praesent aliquet lorem ex, eu dapibus odio varius at. Duis eget tellus porta, consequat lacus vitae, venenatis dolor. Nulla facilisi. In et sollicitudin lacus.</p>
    <p>Donec risus orci, gravida sit amet risus vehicula, aliquet pretium sapien. Nullam sit amet magna non ex bibendum mollis. Nunc vel neque eu augue dignissim congue ut vitae magna. Phasellus eget commodo arcu. Nunc vitae semper dui. Integer venenatis, tellus sit amet interdum pretium, erat neque rhoncus turpis, a aliquam augue ligula eget erat. Nunc placerat, arcu nec mattis fermentum, nisi mauris convallis nunc, ut luctus nunc nisl id ex.</p>
  </div>
  <svg style="position:absolute;left:250px;top:80px" width="120" height="120" viewBox="0 0 120 120">
    <circle cx="60" cy="60" r="54" fill="none" stroke="var(--track)" stroke-width="5"/>
    <circle cx="60" cy="60" r="54" fill="none" stroke="var(--orange)" stroke-width="5" stroke-dasharray="217.1 339.3" transform="rotate(-90 60 60)"/>
    <text x="60" y="69" text-anchor="middle" font-family="Poppins, sans-serif" font-size="25" fill="var(--orange)">64%</text>
  </svg>
  <svg style="position:absolute;left:386px;top:80px" width="120" height="120" viewBox="0 0 120 120">
    <circle cx="60" cy="60" r="54" fill="none" stroke="var(--track)" stroke-width="5"/>
    <circle cx="60" cy="60" r="54" fill="none" stroke="#4a4a4a" stroke-width="5" stroke-dasharray="278.2 339.3" transform="rotate(-90 60 60)"/>
    <text x="60" y="69" text-anchor="middle" font-family="Poppins, sans-serif" font-size="25" fill="#4a4a4a">82%</text>
  </svg>
  <p class="donut-label" style="left:255px;top:210px">Lorem ipsum dolor sit amet, consectetur adipiscing elit. Vivamus eu dui ex. Curabitur dapibus dignissim.</p>
  <p class="donut-label" style="left:391px;top:210px">Lorem ipsum dolor sit amet, consectetur adipiscing elit. Vivamus eu dui ex. Curabitur dapibus dignissim.</p>
  <div class="brand brand--mini" style="left:16px;top:282px"><span class="brand-dot"></span><span class="brand-name">Velmin &amp; Co</span></div>
  <div class="foot-copy"><span><b>© Velmin &amp; Co</b> 2023. All Rights Reserved.</span><span class="page-no">9</span></div>
</div>

<!-- bar chart -->
<div class="slide col-r row-5">
  <h2 class="heading"><b>Heading</b> Goes Here</h2>
  <svg style="position:absolute;left:44px;top:82px" width="240" height="160" viewBox="0 0 240 160" font-family="Poppins, sans-serif" font-size="5" fill="#4a4a4a">
    <g text-anchor="end">
      <text x="12" y="142">0</text><text x="12" y="120">1</text><text x="12" y="98">2</text>
      <text x="12" y="77">3</text><text x="12" y="55">4</text><text x="12" y="33">5</text><text x="12" y="12">6</text>
    </g>
    <line x1="20" y1="140" x2="230" y2="140" stroke="#bdbdbd" stroke-width=".6"/>
    <g fill="var(--orange)">
      <rect x="30" y="46.8" width="9" height="93.2"/><rect x="82.5" y="85.8" width="9" height="54.2"/>
      <rect x="135" y="64.2" width="9" height="75.8"/><rect x="187.5" y="42.5" width="9" height="97.5"/>
    </g>
    <g fill="#5a5a5a">
      <rect x="41" y="88" width="9" height="52"/><rect x="93.5" y="44.7" width="9" height="95.3"/>
      <rect x="146" y="101" width="9" height="39"/><rect x="198.5" y="79.3" width="9" height="60.7"/>
    </g>
    <g fill="#111">
      <rect x="52" y="96.7" width="9" height="43.3"/><rect x="104.5" y="96.7" width="9" height="43.3"/>
      <rect x="157" y="75" width="9" height="65"/><rect x="209.5" y="31.7" width="9" height="108.3"/>
    </g>
    <g font-size="4.5" text-anchor="middle">
      <text x="34.5" y="44">4.3</text><text x="45.5" y="85">2.4</text><text x="56.5" y="94">2</text>
      <text x="87" y="83">2.5</text><text x="98" y="42">4.4</text><text x="109" y="94">2</text>
      <text x="139.5" y="61">3.5</text><text x="150.5" y="98">1.8</text><text x="161.5" y="72">3</text>
      <text x="192" y="40">4.5</text><text x="203" y="76">2.8</text><text x="214" y="29">5</text>
    </g>
    <g text-anchor="middle">
      <text x="46" y="150">Category 1</text><text x="98.5" y="150">Category 2</text>
      <text x="151" y="150">Category 3</text><text x="203.5" y="150">Category 4</text>
    </g>
  </svg>
  <div class="legend" style="top:84px"><span class="legend-key" style="background:var(--orange)"></span>Lorem ipsum dolor sit amet, consectetur adipiscing elit. Vivamus eu dui ex. Curabitur dapibus dignissim dui, in molestie metus.</div>
  <div class="legend" style="top:141px"><span class="legend-key" style="background:#5a5a5a"></span>Lorem ipsum dolor sit amet, consectetur adipiscing elit. Vivamus eu dui ex. Curabitur dapibus dignissim dui, in molestie metus.</div>
  <div class="legend" style="top:198px"><span class="legend-key" style="background:#111"></span>Lorem ipsum dolor sit amet, consectetur adipiscing elit. Vivamus eu dui ex. Curabitur dapibus dignissim dui, in molestie metus.</div>
  <div class="brand brand--mini" style="left:16px;top:282px"><span class="brand-dot"></span><span class="brand-name">Velmin &amp; Co</span></div>
  <div class="foot-copy"><span><b>© Velmin &amp; Co</b> 2023. All Rights Reserved.</span><span class="page-no">10</span></div>
</div>

<!-- contact, light -->
<div class="slide col-l row-6">
  <div class="brand" style="left:48px;top:84px"><span class="brand-dot"></span><span class="brand-name">Velmin &amp; Co</span></div>
  <div class="brand-tag" style="left:48px;top:106px">Advisory for Business Owners</div>
  <h2 class="contact-h">Contact Us</h2>
  <ul class="contact-list">
    <li><svg viewBox="0 0 10 10"><path d="M2 1l2 2-1 1.2c.6 1.2 1.5 2.1 2.8 2.8L7 6l2 2-1.3 1.3C4.5 9 1 5.5.7 2.3z" fill="var(--orange)"/></svg>Phone Number Goes Here</li>
    <li><svg viewBox="0 0 10 10"><circle cx="5" cy="5" r="1.8" fill="none" stroke="var(--orange)" stroke-width="1.1"/><path d="M6.8 3.5v2.3c0 1.4 2.2 1.4 2.2-.8A4 4 0 1 0 7 8.4" fill="none" stroke="var(--orange)" stroke-width="1.1"/></svg>E-Mail Address Goes Here</li>
    <li><svg viewBox="0 0 10 10" fill="none" stroke="var(--orange)" stroke-width=".9"><circle cx="5" cy="5" r="4.2"/><ellipse cx="5" cy="5" rx="1.8" ry="4.2"/><path d="M.8 5h8.4M1.5 3h7M1.5 7h7"/></svg>URL Address Goes Here</li>
  </ul>
  <div class="foot-band"><b>© Velmin &amp; Co</b> 2023. All Rights Reserved.</div>
</div>

<!-- contact, dark -->
<div class="slide slide--dark col-r row-6">
  <div class="photo-dark" role="img" aria-label="Dark photo looking up at office towers"></div>
  <div class="brand" style="left:48px;top:84px"><span class="brand-dot"></span><span class="brand-name">Velmin &amp; Co</span></div>
  <div class="brand-tag" style="left:48px;top:106px">Advisory for Business Owners</div>
  <h2 class="contact-h" style="color:var(--white)">Contact Us</h2>
  <ul class="contact-list">
    <li><svg viewBox="0 0 10 10"><path d="M2 1l2 2-1 1.2c.6 1.2 1.5 2.1 2.8 2.8L7 6l2 2-1.3 1.3C4.5 9 1 5.5.7 2.3z" fill="var(--orange)"/></svg>Phone Number Goes Here</li>
    <li><svg viewBox="0 0 10 10"><circle cx="5" cy="5" r="1.8" fill="none" stroke="var(--orange)" stroke-width="1.1"/><path d="M6.8 3.5v2.3c0 1.4 2.2 1.4 2.2-.8A4 4 0 1 0 7 8.4" fill="none" stroke="var(--orange)" stroke-width="1.1"/></svg>E-Mail Address Goes Here</li>
    <li><svg viewBox="0 0 10 10" fill="none" stroke="var(--orange)" stroke-width=".9"><circle cx="5" cy="5" r="4.2"/><ellipse cx="5" cy="5" rx="1.8" ry="4.2"/><path d="M.8 5h8.4M1.5 3h7M1.5 7h7"/></svg>URL Address Goes Here</li>
  </ul>
  <div class="foot-band foot-band--mint"><b>© Velmin &amp; Co</b> 2023. All Rights Reserved.</div>
</div>

</body>
</html>
```